Introduction Post card

Harbourline Doors
27 Varnel Road
Ruthven Ontario
Gus@harbourlinedoorsco.net
519-555-0143

Dear Leamington Residents

We are excited to announce the launch of Harbourline Doors, your new local source for high-quality windows, doors, and garage doors! As a dedicated member of this community, we are committed to providing exceptional products and services that enhance the beauty and functionality of your home or business.

At Harbourline Doors, we understand that choosing the right windows and doors is essential for energy efficiency, security, and style. That’s why we offer a wide selection of premium products tailored to meet your unique needs. Our expert team is here to guide you through the selection process, ensuring you find the perfect fit for your space.

Our services don’t stop at providing quality products. We pride ourselves on our professional installation process, ensuring that every project is completed with precision and care. Customer satisfaction is our top priority, and we strive to exceed your expectations with every interaction.

We invite you to visit our showroom or contact us to learn more about our offerings. Whether you’re looking to upgrade your home’s curb appeal or enhance its security, we are here to help. Together, let’s make our community a more beautiful place!

Thank you for considering Harbourline Doors for your window, door, and garage door needs. We look forward to serving you!

Warm regards,

Gus
Sales Manager
Harbourline Doors
https://harbourlinedoorsco.net/

```html
<!DOCTYPE html>
<html lang="en">
<head>
<meta charset="utf-8">
<title>Harbourline Doors – Introduction Postcard</title>
<link href="https://fonts.googleapis.com/css2?family=Hind:wght@500;600;700&family=Poppins:wght@400;500;600;700;800&family=Allura&display=swap" rel="stylesheet">
<style>
:root{
  --stage:#b3b3b3;
  --paper:#ffffff;
  --charcoal:#2f2e2c;
  --orange:#f2652a;
  --rust:#c9532a;
  --ink:#1f1f1f;
  --navy:#1d2b45;
  --red:#e01b24;
}
*{margin:0;padding:0;box-sizing:border-box}
html,body{width:820px;height:1200px;overflow:hidden;background:var(--stage)}
body{position:relative;font-family:"Poppins",sans-serif;color:var(--ink)}
.card{position:absolute;left:62px;width:696px;height:497px;background:var(--paper);overflow:hidden}
.card--front{top:71px}
.card--back{top:637px}
.abs{position:absolute}

/* ---------- front ---------- */
.hero-panel{left:28px;top:0;width:311px;height:361px;background:var(--charcoal);border-bottom-right-radius:46px}
.brand{display:flex;align-items:center;gap:10px;font-family:"Hind",sans-serif;font-weight:700;color:#fff;white-space:nowrap}
.brand__mark{border:3px solid #fff;border-radius:4px;flex:none}
.front-brand{left:49px;top:29px;font-size:20px}
.front-brand .brand__mark{width:26px;height:26px}
.hello{left:49px;top:96px;font-family:"Hind",sans-serif;font-weight:700;font-size:26px;color:transparent;-webkit-text-stroke:1px #fff;letter-spacing:1px;display:flex;align-items:center;gap:8px}
.hello::after{content:"";display:block;width:164px;height:1px;background:#fff}
.greeting{left:49px;top:119px;font-family:"Hind",sans-serif;font-weight:700;font-size:23px;color:#fff;white-space:nowrap}
.intro-tab{left:23px;top:150px;width:167px;height:22px;background:var(--orange);border-radius:0 6px 6px 0;color:#fff;font-weight:500;font-size:14px;letter-spacing:3.4px;padding-left:25px;line-height:22px}
.headline{left:47px;top:178px;font-family:"Hind",sans-serif;font-weight:700;line-height:.95;white-space:nowrap}
.headline__name{display:block;color:var(--orange);font-size:40px}
.headline__kind{display:block;color:#fff;font-size:50px}
.trusted{left:49px;top:276px;width:235px;height:66px;border:1.5px solid #8a8a88;border-radius:6px;display:flex;align-items:center;gap:14px;padding-left:12px}
.trusted__text{color:#fff;font-family:"Hind",sans-serif;font-weight:500;font-size:22px;line-height:1.05}

.photo-frame{left:357px;top:29px;width:312px;height:270px;border:2px solid var(--orange);border-bottom:none;border-radius:34px 34px 0 0}
.photo-house{left:370px;top:38px;width:300px;height:250px;border-radius:28px 28px 0 0;background:linear-gradient(180deg,#a9bfd6 0%,#c8cdd2 38%,#8f8274 70%,#4a4035 100%)}
.product{top:248px;width:104px;height:104px;border-radius:50%;border:3px solid var(--orange);background:#fff;padding:3px}
.product__photo{width:100%;height:100%;border-radius:50%}
.product--window{left:364px}.product--window .product__photo{background:linear-gradient(160deg,#e8ebee,#a9b4b0 55%,#6d6f64)}
.product--door{left:463px}.product--door .product__photo{background:linear-gradient(160deg,#cbc6bf,#ece9e4 50%,#7c6e5e)}
.product--garage{left:564px}.product--garage .product__photo{background:linear-gradient(180deg,#c9c8cf,#6d6a6a 55%,#3a3837 80%,#9a9a9a)}
.quality-seal{left:342px;top:237px;width:46px;height:46px;border-radius:50%;background:var(--red);color:#fff;font-weight:700;font-size:9px;line-height:1.1;display:flex;align-items:center;justify-content:center;text-align:center;box-shadow:0 0 0 2px #fff}
.product-label{top:361px;width:100px;font-weight:700;font-size:12px;text-align:center;white-space:nowrap}
.product-label--window{left:364px}
.product-label--door{left:470px}
.product-label--garage{left:569px}
.audience-bar{left:365px;top:379px;width:305px;height:24px;background:var(--charcoal);border-radius:0 6px 6px 0;color:#fff;font-size:16px;text-align:center;line-height:24px;white-space:nowrap}
.audience-bar b{font-weight:700}

.visit{left:28px;top:372px;font-weight:800;font-size:21px;color:var(--orange);white-space:nowrap}
.visit-copy{left:28px;top:395px;font-size:18px;line-height:21px;font-weight:500}
.url-bar{height:25px;background:var(--orange);border-radius:0 10px 10px 0;color:#fff;font-weight:600;letter-spacing:.6px;white-space:nowrap;display:flex;align-items:center;justify-content:center}
.url-bar b{color:var(--charcoal);font-weight:700}
.front-url{left:28px;top:444px;width:259px;font-size:14px}
.contact-icon{width:19px;height:19px;border-radius:50%;background:var(--orange);display:flex;align-items:center;justify-content:center}
.phone-icon{left:310px;top:425px}
.mail-icon{left:310px;top:452px}
.phone{left:336px;top:420px;font-weight:700;font-size:21px;white-space:nowrap}
.email{left:336px;top:452px;font-size:12px;font-weight:500;white-space:nowrap}
.pin-icon{left:508px;top:425px}
.address{left:532px;top:422px;font-size:11.5px;line-height:15px;font-weight:500;white-space:nowrap}
.address__name{color:var(--orange);font-weight:700;font-size:14px;display:block;margin-bottom:2px}

/* ---------- back ---------- */
.frame{left:18px;top:24px;width:660px;height:451px;background:var(--charcoal);border-radius:0 52px 52px 0}
.frame-accent{height:10px;background:var(--orange);left:217px;width:248px}
.frame-accent--top{top:24px}
.frame-accent--bottom{top:465px}
.frame-accent--side{left:18px;top:120px;width:10px;height:246px}
.letter{left:28px;top:35px;width:452px;height:430px;background:var(--paper);border-radius:26px 0 0 0}
.side-brand{left:505px;top:50px;font-size:12px;gap:7px}
.side-brand .brand__mark{width:19px;height:19px;border-width:2px}
.gallery-item{left:512px;width:130px;height:130px;border-radius:50%;border:6px solid var(--rust)}
.gallery-item--home{top:92px;background:linear-gradient(180deg,#d9b8ad 0%,#7b7475 45%,#6b665f 80%,#5e7042)}
.gallery-item--entry{top:205px;background:linear-gradient(90deg,#7e5a45 0%,#3c4740 35%,#d6c43a 60%,#8a5f49 100%)}
.gallery-item--patio{top:324px;background:linear-gradient(180deg,#3d3d3d 0%,#c9cfcf 30%,#a7aca8 70%,#6d6863)}

.salutation{left:57px;top:72px;font-size:16px;line-height:17px}
.salutation strong{display:block;color:var(--orange);font-weight:700;white-space:nowrap}
.salutation-rule{left:262px;top:97px;width:195px;height:2px;background:linear-gradient(90deg,var(--orange) 52%,#9a9a9a 52%)}
.letter-body{left:56px;top:123px;width:404px;font-size:8.7px;line-height:10.7px;text-align:justify}
.letter-body p{margin-bottom:8px}
.signoff{left:56px;top:350px;font-family:"Allura",cursive;font-size:34px;color:var(--navy);line-height:1}
.signer{left:57px;top:384px;font-family:"Hind",sans-serif;font-weight:700;font-size:22px;color:var(--orange);line-height:1}
.signer-role{left:57px;top:407px;font-size:15px;font-weight:500}
.back-url{left:279px;top:405px;width:178px;height:18px;font-size:10px;border-radius:0 8px 8px 0}
</style>
</head>
<body>

<section class="card card--front">
  <div class="abs hero-panel"></div>
  <div class="abs brand front-brand"><span class="brand__mark"></span>HARBOURLINE DOORS</div>
  <div class="abs hello">HELLO</div>
  <div class="abs greeting">LEAMINGTON RESIDENTS</div>
  <div class="abs intro-tab">INTRODUCING</div>
  <h1 class="abs headline"><span class="headline__name">HARBOURLINE</span><span class="headline__kind">DOORS</span></h1>
  <div class="abs trusted">
    <svg width="42" height="40" viewBox="0 0 42 40" aria-hidden="true">
      <path d="M21 3 L31 7 V17 C31 24 26 28 21 30 C16 28 11 24 11 17 V7 Z" fill="#f2652a"/>
      <path d="M16 16 L20 20 L27 12" fill="none" stroke="#fff" stroke-width="2.5" stroke-linecap="round" stroke-linejoin="round"/>
      <path d="M3 20 C5 30 10 36 18 38" fill="none" stroke="#f2652a" stroke-width="4" stroke-linecap="round"/>
      <path d="M39 20 C37 30 32 36 24 38" fill="none" stroke="#f2652a" stroke-width="4" stroke-linecap="round"/>
    </svg>
    <div class="trusted__text">YOUR TRUSTED<br>LOCAL SOURCE</div>
  </div>

  <div class="abs photo-frame"></div>
  <div class="abs photo-house" role="img" aria-label="Photo of a two-storey stone and siding house at dusk with garage"></div>
  <div class="abs product product--window"><div class="product__photo" role="img" aria-label="Photo of a bright bedroom with large windows"></div></div>
  <div class="abs product product--door"><div class="product__photo" role="img" aria-label="Photo of an open white interior door"></div></div>
  <div class="abs product product--garage"><div class="product__photo" role="img" aria-label="Photo of a house with two dark garage doors"></div></div>
  <div class="abs quality-seal">High<br>Quality</div>
  <div class="abs product-label product-label--window">Window</div>
  <div class="abs product-label product-label--door">Doors</div>
  <div class="abs product-label product-label--garage">Garage Doors</div>
  <div class="abs audience-bar">FOR YOUR <b>HOME OR BUSINESS</b></div>

  <div class="abs visit">VISIT OUR SHOWROOM</div>
  <div class="abs visit-copy">or contact us to learn<br>more about our offerings</div>
  <div class="abs url-bar front-url">www.<b>harbourlinedoorsco</b>.net</div>

  <div class="abs contact-icon phone-icon">
    <svg width="11" height="11" viewBox="0 0 24 24" aria-hidden="true"><path d="M6.6 10.8a15.1 15.1 0 0 0 6.6 6.6l2.2-2.2a1 1 0 0 1 1-.25 11.4 11.4 0 0 0 3.6.57 1 1 0 0 1 1 1V20a1 1 0 0 1-1 1A17 17 0 0 1 3 4a1 1 0 0 1 1-1h3.5a1 1 0 0 1 1 1c0 1.250.2 2.450.57 3.6a1 1 0 0 1-.25 1z" fill="#fff"/></svg>
  </div>
  <div class="abs phone">519-555-0143</div>
  <div class="abs contact-icon mail-icon">
    <svg width="11" height="9" viewBox="0 0 22 16" aria-hidden="true"><rect x="1" y="1" width="20" height="14" fill="none" stroke="#fff" stroke-width="2"/><path d="M1 1 L11 9 L21 1" fill="none" stroke="#fff" stroke-width="2"/></svg>
  </div>
  <div class="abs email">Gus@harbourlinedoorsco.net</div>
  <div class="abs contact-icon pin-icon">
    <svg width="10" height="12" viewBox="0 0 20 24" aria-hidden="true"><path d="M10 1a8 8 0 0 1 8 8c0 6-8 14-8 14S2 15 2 9a8 8 0 0 1 8-8z" fill="#fff"/><circle cx="10" cy="9" r="3" fill="#f2652a"/></svg>
  </div>
  <div class="abs address"><span class="address__name">Harbourline Doors</span>27 Varnel Road, Ruthven,<br>Ontario N0R 4K7</div>
</section>

<section class="card card--back">
  <div class="abs frame"></div>
  <div class="abs frame-accent frame-accent--top"></div>
  <div class="abs frame-accent frame-accent--bottom"></div>
  <div class="abs frame-accent frame-accent--side"></div>
  <div class="abs letter"></div>

  <div class="abs brand side-brand"><span class="brand__mark"></span>HARBOURLINE DOORS</div>
  <div class="abs gallery-item gallery-item--home" role="img" aria-label="Photo of a grey house with garage doors"></div>
  <div class="abs gallery-item gallery-item--entry" role="img" aria-label="Photo of a yellow front door in a brick entry"></div>
  <div class="abs gallery-item gallery-item--patio" role="img" aria-label="Photo of a sliding patio door seen from inside"></div>

  <div class="abs salutation">Dear<strong>LEAMINGTON RESIDENTS</strong></div>
  <div class="abs salutation-rule"></div>
  <div class="abs letter-body">
    <p>We are excited to announce the launch of Harbourline Doors, your new local source for high-quality windows, doors, and garage doors! As a dedicated member of this community, we are committed to providing exceptional products and services that enhance the beauty and functionality of your home or business.</p>
    <p>At Harbourline Doors, we understand that choosing the right windows and doors is essential for energy efficiency, security, and style. That’s why we offer a wide selection of premium products tailored to meet your unique needs. Our expert team is here to guide you through the selection process, ensuring you find the perfect fit for your space.</p>
    <p>Our services don’t stop at providing quality products. We pride ourselves on our professional installation process, ensuring that every project is completed with precision and care. Customer satisfaction is our top priority, and we strive to exceed your expectations with every interaction.</p>
    <p>We invite you to visit our showroom or contact us to learn more about our offerings. Whether you’re looking to upgrade your home’s curb appeal or enhance its security, we are here to help. Together, let’s make our community a more beautiful place!</p>
    <p>Thank you for considering Harbourline Doors for your window, door, and garage door needs. We look forward to serving you!</p>
  </div>
  <div class="abs signoff">Warm Regards</div>
  <div class="abs signer">GUS</div>
  <div class="abs signer-role">Sales Manager</div>
  <div class="abs url-bar back-url">www.<b>harbourlinedoorsco</b>.net</div>
</section>

</body>
</html>
```